Business Cards that are elegant and wow

I want to create and print business cards that represent my brand and stand out from the rest. We want to ensure they stay in our branding and the integrity is not lost. I am happy to look at different shapes like square etc.

It will be printed on very thick cards and will be stylish .

I want to create and print business cards that represent my brand and stand out from the rest. We want to ensure they stay in ur branding and the integrity is not lost. I am happy to look at different shapes like square etc.

Target Market(s)

real estate professionals

Industry/Entity Type

Real Estate

Contact Information for Business Card

Maren Holt
hello@brightfernrealty.com.au
brightfernrealty.com.au
0487 316 252 (SMS)

Colors

Designer to choose colors to be used in the design.

Requirements
Must have
• My logo
• email
• website
• Name
Nice to have
• I like the idea of printing with foil or spot gloss. You want it to stand out in a sea.
Should not have
• I would like you to stay in my colour themes. Don't change the colour of my logo

```html
<!DOCTYPE html>
<html lang="en">
<head>
<meta charset="utf-8">
<title>Bright Fern Realty – Business Cards</title>
<link rel="stylesheet" href="https://fonts.googleapis.com/css2?family=Lato:wght@400;700&display=swap">
<style>
  :root {
    --backdrop: #a9a9a9;
    --sky: #16b3ee;
    --sky-deep: #0aa6e6;
    --magenta: #e8137d;
    --paper: #ffffff;
  }
  * { box-sizing: border-box; margin: 0; padding: 0; }
  html, body { width: 1200px; height: 930px; overflow: hidden; }
  body {
    background: radial-gradient(circle at 45% 40%, #c4c4c4 0%, var(--backdrop) 55%, #8e8e8e 100%);
    font-family: "Lato", Arial, sans-serif;
    position: relative;
  }
  .card {
    position: absolute;
    width: 560px;
    height: 320px;
    border-radius: 22px;
    box-shadow: 0 6px 16px rgba(0,0,0,0.25);
  }
  .card-front {
    left: 80px; top: 100px;
    background: linear-gradient(135deg, var(--sky) 0%, var(--sky-deep) 100%);
    display: flex; align-items: center; justify-content: center;
  }
  .card-back {
    left: 560px; top: 500px;
    background: var(--paper);
  }
  .brand {
    display: flex; align-items: center; gap: 10px;
    font-weight: 700; letter-spacing: 1px; text-transform: uppercase;
  }
  .brand-dot { width: 34px; height: 34px; border-radius: 50%; flex: none; }
  .card-front .brand { color: var(--paper); font-size: 30px; }
  .card-front .brand-dot { border: 3px solid var(--paper); width: 44px; height: 44px; }
  .card-back .brand {
    position: absolute; right: 40px; top: 40px;
    color: var(--magenta); font-size: 20px;
  }
  .card-back .brand-dot { border: 3px solid var(--sky); }
  .holder { position: absolute; left: 34px; top: 176px; }
  .holder-name { color: var(--sky); font-size: 27px; font-weight: 700; letter-spacing: 1px; text-transform: uppercase; line-height: 1; }
  .holder-role { color: var(--magenta); font-size: 15px; margin-top: 4px; }
  .divider { position: absolute; left: 34px; right: 34px; top: 254px; height: 1.5px; background: var(--sky); }
  .contact {
    position: absolute; left: 34px; right: 20px; top: 270px;
    font-size: 10.8px; color: var(--magenta); white-space: nowrap;
  }
  .contact .label, .contact .sep { color: var(--sky); }
</style>
</head>
<body>
  <section class="card card-front" aria-label="Card front">
    <div class="brand"><span class="brand-dot"></span>Bright Fern Realty</div>
  </section>

  <section class="card card-back" aria-label="Card back">
    <div class="brand"><span class="brand-dot"></span>Bright Fern Realty</div>
    <div class="holder">
      <p class="holder-name">Maren Holt</p>
      <p class="holder-role">Director at Bright Fern Realty</p>
    </div>
    <div class="divider"></div>
    <p class="contact">
      <span class="label">P :</span> 0487 316 252 (SMS) <span class="sep">|</span>
      <span class="label">E :</span> hello@brightfernrealty.com.au <span class="sep">|</span>
      <span class="label">W :</span> www.brightfernrealty.com.au
    </p>
  </section>
</body>
</html>
```